Business Card for boutique psychology business

Business card for boutique psychology practice in Melbourne. I want them to be relatively simply with the logo and backing colour taking up the front side. Then, text on the back, with my name; professional title (Clinical Psychologist); website - torvinpsychology.com.au; email: hello@torvinpsychology.com.au; insta: @torvin.psychology.emdr
Back should also have the words: Connect. Integrate. Evolve
Fonts used for logo are: Mikea Demo and Gotham Medium. Use something for back text that will compliment these.
Brand colours uploaded below. I'd like to see options in both olive and blush.

```html
<!DOCTYPE html>
<html lang="en">
<head>
<meta charset="utf-8">
<title>torvin psychology + EMDR — business card</title>
<link rel="stylesheet" href="https://fonts.googleapis.com/css2?family=Josefin+Sans:wght@300&family=Montserrat:wght@600;700&display=swap">
<style>
  :root {
    --olive: #4a5233;
    --olive-soft: #5b6342;
    --blush: #ecd3c2;
    --blush-deep: #e3c3ae;
    --backdrop: #e9e6e1;
    --card-w: 620px;
    --card-h: 376px;
  }
  * { box-sizing: border-box; margin: 0; padding: 0; }
  html, body { width: 1200px; height: 901px; overflow: hidden; }
  body {
    background: var(--backdrop);
    display: flex;
    flex-direction: column;
    align-items: center;
    justify-content: center;
    gap: 48px;
  }
  .card {
    position: relative;
    width: var(--card-w);
    height: var(--card-h);
    border-radius: 22px;
    overflow: hidden;
    box-shadow: 0 6px 18px rgba(0,0,0,0.12);
  }
  .card__bg { position: absolute; inset: 0; width: 100%; height: 100%; }
  .brand-name {
    font-family: "Josefin Sans", sans-serif;
    font-weight: 300;
    line-height: 1;
    letter-spacing: 2px;
  }
  .brand-descriptor {
    font-family: "Montserrat", sans-serif;
    font-weight: 700;
    letter-spacing: 1px;
  }

  /* Front: olive with tagline */
  .card--front { background: var(--olive); }
  .card--front .brand-block {
    position: absolute; left: 210px; top: 120px; color: var(--blush);
  }
  .card--front .brand-name { font-size: 92px; }
  .card--front .brand-descriptor { font-size: 19px; margin-top: 6px; padding-left: 6px; }
  .tagline {
    position: absolute; left: 52px; bottom: 42px; right: 40px;
    display: flex; align-items: center; gap: 20px;
    font-family: "Josefin Sans", sans-serif; font-weight: 300;
    font-size: 38px; color: var(--blush); letter-spacing: 2px;
  }
  .tagline__dot { width: 8px; height: 8px; border-radius: 50%; background: var(--blush); }

  /* Back: contact details */
  .card--back { background: var(--blush); }
  .card--back .brand-block {
    position: absolute; left: 48px; top: 40px; color: var(--blush);
  }
  .card--back .brand-name { font-size: 88px; }
  .card--back .brand-descriptor { font-size: 19px; margin-top: 4px; padding-left: 6px; }
  .practitioner {
    position: absolute; right: 36px; top: 176px; text-align: right; color: var(--olive);
  }
  .practitioner__name {
    font-family: "Josefin Sans", sans-serif; font-weight: 300;
    font-size: 30px; letter-spacing: 2px;
  }
  .practitioner__title {
    font-family: "Montserrat", sans-serif; font-weight: 700;
    font-size: 15px; margin-top: 2px;
  }
  .contact-list {
    position: absolute; left: 48px; bottom: 28px; list-style: none;
    font-family: "Montserrat", sans-serif; font-weight: 600;
    font-size: 15px; color: var(--olive);
  }
  .contact-list li { display: flex; align-items: center; gap: 10px; height: 23px; }
  .contact-list svg { width: 15px; height: 15px; flex: none; }
  .contact-list .social-mark {
    width: 13px; height: 13px; border: 2px solid var(--olive); border-radius: 3px; flex: none; margin: 0 1px;
  }
</style>
</head>
<body>

  <section class="card card--front" aria-label="Card front">
    <svg class="card__bg" viewBox="0 0 620 376" preserveAspectRatio="none" aria-hidden="true">
      <path d="M0 0 H380 C300 40 180 80 0 104 Z" fill="var(--blush)"/>
      <path d="M0 104 C180 80 300 40 380 0 H410 C320 55 190 98 0 122 Z" fill="var(--olive-soft)" opacity="0.6"/>
    </svg>
    <div class="brand-block">
      <div class="brand-name">torvin</div>
      <div class="brand-descriptor">psychology + EMDR</div>
    </div>
    <p class="tagline">
      <span>Connect</span><span class="tagline__dot"></span>
      <span>Integrate</span><span class="tagline__dot"></span>
      <span>Evolve</span>
    </p>
  </section>

  <section class="card card--back" aria-label="Card back">
    <svg class="card__bg" viewBox="0 0 620 376" preserveAspectRatio="none" aria-hidden="true">
      <path d="M0 0 H620 V30 C540 50 480 90 420 130 C330 195 200 225 0 232 Z" fill="var(--olive)"/>
      <path d="M620 30 C540 50 480 90 420 130 C500 85 560 62 620 54 Z" fill="var(--blush-deep)" opacity="0.7"/>
    </svg>
    <div class="brand-block">
      <div class="brand-name">torvin</div>
      <div class="brand-descriptor">psychology + EMDR</div>
    </div>
    <div class="practitioner">
      <div class="practitioner__name">Daniel Reyes</div>
      <div class="practitioner__title">Clinical Psychologist</div>
    </div>
    <ul class="contact-list">
      <li>
        <svg viewBox="0 0 16 16" aria-hidden="true"><path d="M4 1.5l2.5 3-1.5 1.8c.8 1.8 2 3 3.8 3.8L10.6 8.6l3 2.5-1.4 2.6C7 13.6 2.4 9 2.4 3z" fill="var(--olive)"/></svg>
        <span>0400 000 123</span>
      </li>
      <li>
        <svg viewBox="0 0 16 16" aria-hidden="true"><rect x="1.5" y="3.5" width="13" height="9" fill="none" stroke="var(--olive)" stroke-width="1.6"/><path d="M1.5 3.5L8 9l6.5-5.5" fill="none" stroke="var(--olive)" stroke-width="1.6"/></svg>
        <span>hello@torvinpsychology.com.au</span>
      </li>
      <li>
        <svg viewBox="0 0 16 16" aria-hidden="true"><circle cx="8" cy="8" r="6.5" fill="none" stroke="var(--olive)" stroke-width="1.6"/><ellipse cx="8" cy="8" rx="2.8" ry="6.5" fill="none" stroke="var(--olive)" stroke-width="1.3"/><path d="M1.5 8h13" stroke="var(--olive)" stroke-width="1.3"/></svg>
        <span>torvinpsychology.com.au</span>
      </li>
      <li>
        <span class="social-mark" aria-hidden="true"></span>
        <span>@torvin.psychology.emdr</span>
      </li>
    </ul>
  </section>

</body>
</html>
```